4th Generation Family Business Needs a New Card Design!

We are a family owned 4th Generation company. We are based in the Sydney, Australia area and we are desperately in need of a more modern and classy card. We are monumental masons who design, supply & erect lasting memorials throughout cemeteries in Sydney. Our customers are normally in a period of grieving. I have attached logo files that will need to be implemented on the card. Company was established 1935. Australian Owned and Operated. Card needs to be designed to PRINTLY.com specification.

Target Market(s)

Our target market is based upon people that a grieving for family members that have passed away. We also deal with alot of companies that own and operate cemeteries.

Industry/Entity Type

Business

Contact Information for Business Card

Oliver Brantley, Operations Manager, 0417552908, oliver@hollowaystoneworks.com.au
Martin Brantley, Director, 0431906627, martin@hollowaystoneworks.com.au
Phone # 02 9634 2258
Website: www.hollowaystoneworks.com.au
Address: Suite 17, 8 Calloway Lane, East Penrose, Sydney NSW 2290

Font styles to use
Serif
Decorative
Script

Requirements
Must have
• Would like to see the logo nicely implemented with a modern design. Embossed lettering would be a nice additive.

```html
<!DOCTYPE html>
<html lang="en">
<head>
<meta charset="utf-8">
<title>Holloway Stoneworks – Business Card</title>
<link href="https://fonts.googleapis.com/css2?family=Roboto+Condensed:wght@400;500&display=swap" rel="stylesheet">
<style>
  :root {
    --backdrop: #e6e6e8;
    --card-black: #222224;
    --gold: #e3bf3e;
    --gold-light: #edd063;
    --ink: #2a2a2a;
    --cream-top: #fbf6e2;
    --cream-mid: #ffffff;
    --cream-bottom: #f3e6b4;
  }
  html, body {
    margin: 0;
    padding: 0;
    width: 1200px;
    height: 810px;
    overflow: hidden;
    background: var(--backdrop);
    font-family: "Roboto Condensed", "Arial Narrow", sans-serif;
  }
  .canvas {
    position: relative;
    width: 1200px;
    height: 810px;
  }
  .card {
    position: absolute;
    top: 135px;
    width: 280px;
    height: 540px;
    box-shadow: 0 6px 22px rgba(0,0,0,0.18);
  }
  .card-front {
    left: 300px;
    background: var(--card-black);
  }
  .card-back {
    left: 620px;
    background: linear-gradient(180deg, var(--cream-top) 0%, var(--cream-mid) 40%, var(--cream-mid) 55%, var(--cream-bottom) 100%);
  }
  .stone-panel {
    position: absolute;
    inset: 0;
  }
  .front-content {
    position: absolute;
    inset: 0;
    text-align: center;
    color: var(--ink);
  }
  .person-name {
    margin: 78px 0 0;
    font-size: 21px;
    font-weight: 500;
    letter-spacing: 0.2px;
  }
  .person-role {
    margin: 4px 0 0;
    font-size: 11px;
  }
  .front-brand {
    margin: 62px auto 0;
    width: 190px;
    font-size: 26px;
    font-weight: 500;
    line-height: 1.15;
    color: var(--ink);
  }
  .contact-block {
    margin: 0;
    font-size: 12.5px;
    line-height: 1.55;
  }
  .contact-mobile { margin-top: 80px; }
  .contact-office { margin-top: 18px; }
  .contact-address { margin-top: 18px; }
  .back-brand {
    position: absolute;
    left: 0;
    right: 0;
    top: 238px;
    text-align: center;
  }
  .back-brand-mark {
    display: block;
    width: 14px;
    height: 14px;
    margin: 0 auto 14px;
    background: var(--gold);
  }
  .back-brand-name {
    margin: 0;
    font-size: 30px;
    font-weight: 500;
    line-height: 1.15;
    color: var(--ink);
  }
</style>
</head>
<body>
  <main class="canvas">
    <section class="card card-front">
      <svg class="stone-panel" width="280" height="540" viewBox="0 0 280 540" aria-hidden="true">
        <defs>
          <linearGradient id="goldFill" x1="0" y1="0" x2="1" y2="1">
            <stop offset="0" stop-color="#e1bc36"/>
            <stop offset="0.5" stop-color="#edd063"/>
            <stop offset="1" stop-color="#e0ba38"/>
          </linearGradient>
        </defs>
        <path d="M34 515 L34 110 Q34 48 140 40 Q246 48 246 110 L246 515 Z" fill="url(#goldFill)"/>
        <rect x="22" y="505" width="236" height="14" fill="url(#goldFill)"/>
      </svg>
      <div class="front-content">
        <h1 class="person-name">Oliver Brantley</h1>
        <p class="person-role">Operations Manager</p>
        <p class="front-brand">Holloway Stoneworks</p>
        <p class="contact-block contact-mobile">M: 0417552908<br>E: oliver@hollowaystoneworks.com.au</p>
        <p class="contact-block contact-office">P: 02 9634 2258<br>W: www.hollowaystoneworks.com.au</p>
        <p class="contact-block contact-address">Suite 17, 8 Calloway Lane<br>East Penrose, Sydney NSW 2290</p>
      </div>
    </section>

    <section class="card card-back">
      <div class="back-brand">
        <span class="back-brand-mark"></span>
        <p class="back-brand-name">Holloway<br>Stoneworks</p>
      </div>
    </section>
  </main>
</body>
</html>
```